KVRo Business Cards

We need a business card design. We are a Technology (Audio Visual) design, sales and installation company. Looking for a double sided design, clean

Contact Information for Business Card

Clean, modern look, 2 sided

Font styles to use
Sans Serif

```html
<!DOCTYPE html>
<html lang="en">
<head>
<meta charset="utf-8">
<title>KVRo Business Cards</title>
<link href="https://fonts.googleapis.com/css2?family=Arimo:wght@400;700&display=swap" rel="stylesheet">
<style>
  :root {
    --backdrop: #4a4440;
    --card: #121214;
    --orange: #f39a1e;
    --white: #ffffff;
  }
  * { box-sizing: border-box; margin: 0; padding: 0; }
  html, body {
    width: 1200px; height: 716px; overflow: hidden;
    background: var(--backdrop);
    font-family: "Arimo", Arial, sans-serif;
  }
  .canvas {
    position: relative; width: 1200px; height: 716px;
    display: flex; align-items: center; justify-content: center; gap: 40px;
  }
  .card {
    position: relative; width: 540px; height: 309px;
    background: var(--card);
    box-shadow: 0 10px 28px rgba(0,0,0,.45);
    color: var(--white);
  }
  .wordmark {
    font-weight: 700; color: var(--white); letter-spacing: -1px; line-height: 1;
  }
  .card-front .wordmark {
    position: absolute; left: 0; right: 0; top: 50%;
    transform: translateY(-50%); text-align: center; font-size: 92px;
  }
  .card-back .wordmark {
    position: absolute; right: 44px; top: 150px; font-size: 60px;
  }
  .name-block {
    position: absolute; left: 58px; top: 40px;
    padding-left: 14px; border-left: 4px solid var(--orange);
  }
  .name { color: var(--orange); font-weight: 700; font-size: 17px; letter-spacing: .5px; }
  .role { font-size: 11px; letter-spacing: 1px; margin-top: 2px; }
  .guide-line {
    position: absolute; left: 58px; top: 84px; width: 1px; height: 132px;
    background: var(--orange);
  }
  .contacts {
    position: absolute; left: 44px; top: 222px; list-style: none;
    font-size: 12px; letter-spacing: 1px; line-height: 19px;
  }
  .contacts li { display: flex; align-items: center; gap: 8px; }
  .contacts svg { width: 10px; height: 10px; fill: var(--orange); flex: none; }
  .address {
    position: absolute; right: 44px; bottom: 26px;
    padding-right: 12px; border-right: 3px solid var(--orange);
    text-align: right; font-size: 13px; line-height: 18px; letter-spacing: .5px;
  }
</style>
</head>
<body>
<main class="canvas">
  <section class="card card-front">
    <div class="wordmark">KVRo</div>
  </section>

  <section class="card card-back">
    <div class="name-block">
      <div class="name">DYLAN MARSH</div>
      <div class="role">President, CEO</div>
    </div>
    <div class="guide-line"></div>
    <ul class="contacts">
      <li><svg viewBox="0 0 10 10"><path d="M2 0.5l2 2-1 1.2a6 6 0 0 0 3.3 3.3l1.2-1 2 2-1.3 1.5C5 9.5.5 5 .5 1.8z"/></svg>555.201.4478</li>
      <li><svg viewBox="0 0 10 10"><path d="M0 2h10v6H0z M0 2l5 3.5L10 2" stroke="#121214" stroke-width=".8"/></svg>info@kvro.com.au</li>
      <li><svg viewBox="0 0 10 10"><circle cx="5" cy="5" r="5"/><path d="M0 5h10M5 0c-2.5 3-2.5 7 0 10M5 0c2.5 3 2.5 7 0 10" stroke="#121214" stroke-width=".7" fill="none"/></svg>www.kvro.com.au</li>
    </ul>
    <div class="wordmark">KVRo</div>
    <address class="address" style="font-style:normal">
      214 Harbor Lane, STE<br>900 Fairview,<br>CA 90210
    </address>
  </section>
</main>
</body>
</html>
```